New business needs a slick but classy, conservative and elegant Legal Letterhead

We need a new letterhead for a law firm that is slick but very classy and also understated.

The name of the firm is K.L. Marlow Lawyers.

All information about the Law firm should appear at the top of the page. Please no firm information in the footer.

It should have a clean, neat look. No watermarks or bold graphics please.

Info should include the name of the law firm, both the street address and postal address, the phone number and the fax number, the names of the principals, the website. We have attached a word document that contains the relevant information.

We have attached a copy of the business card for further information purposes.

We also need a law society logo to appear (probably on the bottom right hand side of the letterhead?) that states our affiliation to the law society. It is attached and must not be altered in any way. It can be small.

The only footer text we require is as worded in the attached information document.

We would like to see designs that use red and white - in an understated, elegant style - not too modern or too gaudy looking.

The final design should communicate that we mean business and that we are to be trusted.
Updates

Please insert firm's name K.L. Marlow Lawyers on letterhead! I have removed Marlow logo as designers were using it instead of the name of the firm. Thank you!

Industry/Entity Type

Legal

Font styles to use
Serif

Colors
ec1f27
ffffff

Requirements
Must have
• All information contained in the word document attached - firm details, law society affiliation logo, firm name & firm logo, principals' names.
Should not have
• watermarks
• no firm details in footer

```html
<!DOCTYPE html>
<html lang="en">
<head>
<meta charset="utf-8">
<title>K.L. Marlow Lawyers – Letterhead</title>
<link rel="stylesheet" href="https://fonts.googleapis.com/css2?family=Libre+Baskerville:ital,wght@0,400;0,700;1,400&display=swap">
<style>
  :root {
    --brand-red: #ec1f27;
    --deep-red: #b3141b;
    --ink: #3a3a3a;
    --muted: #6b6b6b;
    --paper: #ffffff;
  }
  * { margin: 0; padding: 0; box-sizing: border-box; }
  html, body { width: 891px; height: 1200px; overflow: hidden; background: var(--paper); }
  .letterhead {
    position: relative;
    width: 891px;
    height: 1200px;
    background: var(--paper);
    font-family: "Libre Baskerville", "Times New Roman", serif;
    color: var(--ink);
  }
  .header-band { position: absolute; top: 0; left: 0; width: 891px; height: 40px; }
  .brand-mark {
    position: absolute;
    top: 58px;
    right: 40px;
    font-size: 30px;
    font-weight: 700;
    letter-spacing: 1px;
    color: var(--brand-red);
    white-space: nowrap;
  }
  .firm-details { position: absolute; top: 84px; left: 53px; width: 520px; }
  .firm-name {
    font-size: 19px;
    font-weight: 700;
    color: var(--brand-red);
    letter-spacing: 0.5px;
    padding-bottom: 5px;
    border-bottom: 1px solid var(--brand-red);
    width: 300px;
  }
  .detail-label {
    margin-top: 6px;
    font-size: 9px;
    color: var(--brand-red);
  }
  .detail-line { font-size: 9px; line-height: 13px; color: var(--muted); }
  .contact-block { margin-top: 8px; }
  .footer-rule {
    position: absolute;
    left: 0;
    top: 1146px;
    width: 770px;
    height: 2px;
    background: var(--brand-red);
  }
  .footer-note {
    position: absolute;
    left: 18px;
    top: 1166px;
    font-size: 13px;
    font-style: italic;
    color: var(--muted);
  }
  .affiliation-badge { position: absolute; left: 790px; top: 1130px; width: 60px; height: 56px; }
</style>
</head>
<body>
<main class="letterhead">
  <svg class="header-band" viewBox="0 0 891 40" aria-hidden="true">
    <polygon points="440,0 891,0 891,14 452,14" fill="var(--brand-red)"/>
    <polygon points="630,0 891,0 891,36 650,36" fill="var(--brand-red)"/>
    <polygon points="780,14 891,14 891,36 790,36" fill="var(--deep-red)"/>
    <rect x="0" y="18" width="640" height="2" fill="var(--brand-red)"/>
  </svg>

  <div class="brand-mark">MARLOW</div>

  <section class="firm-details">
    <h1 class="firm-name">K.L. MARLOW LAWYERS</h1>
    <p class="detail-label">Address:</p>
    <p class="detail-line">Suite 4, 18 Harlow Street</p>
    <p class="detail-line">PO Box 212, Eastbrook NSW 2150</p>
    <p class="detail-label">Principals:</p>
    <p class="detail-line">Kevin Marlow &amp; Laura Marlow</p>
    <div class="contact-block">
      <p class="detail-line">T (02) 5550 0142</p>
      <p class="detail-line">F (02) 5550 0143</p>
      <p class="detail-line">www.klmarlow.com.au</p>
    </div>
  </section>

  <div class="footer-rule"></div>
  <p class="footer-note">Liability limited by a scheme approved under Professional Standards</p>

  <svg class="affiliation-badge" viewBox="0 0 60 56" role="img" aria-label="Law society affiliation badge">
    <rect x="4" y="4" width="52" height="48" rx="4" fill="var(--brand-red)" opacity="0.85"/>
  </svg>
</main>
</body>
</html>
```